We are full service plumbing contractors that are capable of performing all of your plumbing need...

A clean, crisp website that conveys we can handle any plumbing from drain cleaning, repairs, to new construction. But emphasis on Leak detection, under-slab and underground water service leaks, repairs, and reroutes. Leak detection by acoustical, Thermal, or tracer gas , methods.Also emphasize advanced drain cleaning technologies and equipment. Don't just poke ahole in the drain blockage, Clean the pipe, with our High pressure hydrojetters, or Chain knocker drain cables that expand to the width of the pipe being cleaned.

Number of Pages Required

5+ page

Font styles to use
Sans Serif

Requirements
Should not have
• Canned photos

```html
<!DOCTYPE html>
<html lang="en">
<head>
<meta charset="utf-8">
<title>Keelwater Plumbing</title>
<link href="https://fonts.googleapis.com/css2?family=Montserrat:wght@400;500;600;700&family=Michroma&family=Russo+One&family=Kaushan+Script&display=swap" rel="stylesheet">
<style>
:root{
  --blue:#1d77c8;
  --blue-dark:#0f5ea6;
  --red:#e3262d;
  --red-dark:#b71c22;
  --ink:#333;
  --muted:#666;
  --light:#f2f2f2;
  --gray:#ececec;
  --footer:#2e2e2e;
  --footer-bar:#232323;
  --white:#fff;
}
*{box-sizing:border-box;margin:0;padding:0}
html,body{width:1200px;height:4138px;overflow:hidden}
body{position:relative;font-family:"Montserrat",sans-serif;color:var(--ink);background:var(--white)}
.abs{position:absolute}
/* header */
.topbar{left:0;top:0;width:1200px;height:97px;background:var(--white)}
.brand{left:140px;top:18px;display:flex;align-items:center;gap:10px;font-family:"Montserrat",sans-serif;font-weight:700;font-size:26px;color:var(--blue-dark);z-index:5}
.brand-dot{width:22px;height:22px;border-radius:50%;background:var(--red)}
.call{left:672px;top:30px;display:flex;align-items:center;gap:10px;font-size:15px;font-weight:700;color:var(--ink)}
.call span{color:var(--blue)}
.call-ico{width:30px;height:30px;border:2px solid var(--blue);border-radius:50%;display:flex;align-items:center;justify-content:center}
.socials{left:910px;top:30px;display:flex;gap:9px}
.socials i{display:block;width:28px;height:28px;border-radius:50%;border:2px solid var(--blue)}
.navbar{left:0;top:97px;width:1200px;height:34px;background:var(--blue)}
.nav{left:366px;top:97px;height:34px;display:flex;align-items:center;gap:34px;font-size:13px;font-weight:600;color:var(--white);letter-spacing:.5px}
.quote-btn{left:905px;top:84px;width:146px;height:48px;background:var(--red);color:var(--white);font-weight:700;font-size:16px;display:flex;align-items:center;justify-content:center}
/* hero */
.hero{left:0;top:131px;width:1200px;height:590px;background:linear-gradient(120deg,#3a4a55 0%,#5f6e73 40%,#8b8f86 70%,#4b5257 100%)}
.hero-shade{left:0;top:131px;width:1200px;height:590px;background:linear-gradient(90deg,rgba(0,0,0,.45),rgba(0,0,0,.05) 60%)}
.hero-title{left:132px;top:286px;font-family:"Russo One",sans-serif;font-size:40px;line-height:46px;color:var(--white);letter-spacing:1px}
.hero-sub{left:132px;top:390px;font-size:15px;color:var(--white)}
.hero-btn{left:132px;top:430px;width:170px;height:38px;background:var(--blue);color:var(--white);font-size:14px;font-weight:700;display:flex;align-items:center;justify-content:center}
.form{left:710px;top:200px;width:344px;height:362px;background:rgba(29,119,200,.85)}
.form h3{height:46px;background:var(--blue-dark);color:var(--white);font-size:22px;font-weight:700;display:flex;align-items:center;justify-content:center}
.field{margin:0 24px;height:42px;border-bottom:1px solid rgba(255,255,255,.5);font-size:10px;color:var(--white);display:flex;align-items:flex-end;padding-bottom:6px;letter-spacing:.5px}
.field.tall{height:60px}
.submit{margin:26px 24px 0;height:32px;background:var(--red);color:var(--white);font-size:14px;font-weight:700;display:flex;align-items:center;justify-content:center}
.wave{left:0;top:560px;width:1200px;height:165px}
/* features */
.feature{width:300px;text-align:center;top:826px}
.feature .ico{width:100px;height:100px;border-radius:50%;margin:0 auto;display:flex;align-items:center;justify-content:center}
.feature h4{margin-top:28px;font-size:14px;font-weight:700;color:var(--ink)}
.feature p{margin:8px auto 0;width:230px;font-size:12.5px;line-height:18px;color:var(--muted)}
.band{left:0;top:1116px;width:1200px;height:76px;background:var(--light)}
/* service rows */
.panel{left:0;width:1200px;height:514px}
.photo{height:514px}
.svc-title{font-family:"Michroma",sans-serif;font-size:23px;letter-spacing:2px;color:var(--ink)}
.svc-title em{display:block;font-family:"Kaushan Script",cursive;font-style:normal;font-size:40px;letter-spacing:0;color:var(--red);margin:-2px 0 0 136px}
.rule{width:36px;height:3px;background:var(--red)}
.copy{width:380px;font-size:12.5px;line-height:22px;color:var(--muted)}
.copy p+p{margin-top:20px}
.more{width:116px;height:36px;border-radius:18px;background:var(--red);color:var(--white);font-size:11px;font-weight:700;display:flex;align-items:center;justify-content:center;gap:6px}
.on-blue .svc-title,.on-blue .copy{color:var(--white)}
.on-blue .svc-title em{color:var(--white)}
/* additional */
.additional{left:0;top:2718px;width:1200px;height:670px;background:var(--gray)}
.sec-title{width:1200px;text-align:center;font-family:"Michroma",sans-serif;font-size:22px;letter-spacing:2px;color:var(--ink)}
.sec-title em{font-family:"Kaushan Script",cursive;font-style:normal;font-size:38px;letter-spacing:0;color:var(--red)}
.svc{width:240px}
.svc .badge{width:64px;height:64px;border-radius:50%;background:var(--white);box-shadow:0 2px 6px rgba(0,0,0,.12);display:flex;align-items:center;justify-content:center}
.svc h5{margin-top:16px;font-size:13px;font-weight:700;line-height:18px;color:var(--ink)}
.svc p{margin-top:10px;font-size:12px;line-height:19px;color:var(--muted)}
.all-card{left:756px;top:3127px;width:302px;height:186px;background:var(--white);text-align:center;box-shadow:0 2px 8px rgba(0,0,0,.08)}
.all-card h5{margin-top:26px;font-family:"Michroma",sans-serif;font-size:14px;letter-spacing:2px;color:var(--blue-dark)}
.all-card p{margin:12px auto 0;width:230px;font-size:12.5px;line-height:19px;color:var(--muted)}
.all-card .more{margin:18px auto 0;width:128px}
/* testimonials */
.tcard{top:3542px;width:274px;height:206px;background:var(--light);text-align:center;padding:0 22px}
.tcard.active{background:var(--blue);color:var(--white)}
.tcard .q{position:absolute;left:20px;top:14px;font-family:Georgia,serif;font-size:44px;line-height:40px;color:#c9c9c9}
.tcard.active .q{color:rgba(255,255,255,.5)}
.tcard blockquote{margin-top:54px;font-size:12px;line-height:18px;color:var(--muted)}
.tcard.active blockquote,.tcard.active .co{color:var(--white)}
.tcard h6{margin-top:20px;font-size:12.5px;font-weight:600;letter-spacing:1px;text-transform:uppercase}
.tcard .co{margin-top:4px;font-size:11px;color:var(--muted)}
.arrow{top:3630px}
.dots{left:585px;top:3783px;display:flex;gap:6px}
.dots i{display:block;width:9px;height:9px;border-radius:50%;border:1.5px solid var(--blue)}
.dots i.on{background:var(--blue)}
/* footer */
.footer{left:0;top:3863px;width:1200px;height:227px;background:var(--footer)}
.fcol{top:3900px;color:#ccc;font-size:12px}
.fcol h6{font-size:13.5px;font-weight:700;color:var(--white);margin-bottom:14px}
.fcol li{list-style:none;height:28px;border-bottom:1px solid #444;display:flex;align-items:center;width:180px}
.fcol .row{display:flex;gap:10px;align-items:flex-start;margin-bottom:10px;line-height:17px}
.news-in{margin-top:6px;width:212px;height:32px;border-radius:16px;background:var(--white);font-size:11px;color:#999;display:flex;align-items:center;justify-content:space-between;padding:0 14px}
.fsocial{margin-top:14px;display:flex;gap:8px}
.fsocial i{display:block;width:24px;height:24px;border-radius:50%;border:1px solid #777}
.footbar{left:0;top:4090px;width:1200px;height:48px;background:var(--footer-bar);color:#aaa;font-size:12px;display:flex;align-items:center;justify-content:center}
</style>
</head>
<body>

<!-- header -->
<div class="abs topbar"></div>
<div class="abs navbar"></div>
<div class="abs brand"><span class="brand-dot"></span>Keelwater Plumbing</div>
<div class="abs call">
  <span class="call-ico"><svg width="14" height="14" viewBox="0 0 24 24"><path d="M6.6 10.8a15.1 15.1 0 006.6 6.6l2.2-2.2a1 1 0 011-.25 11.4 11.4 0 003.6.57 1 1 0 011 1V20a1 1 0 01-1 1A17 17 0 013 4a1 1 0 011-1h3.5a1 1 0 011 1c0 1.25.2 2.45.57 3.57a1 1 0 01-.25 1z" fill="#1d77c8"/></svg></span>
  CALL : <span>+1 555 014 2290</span>
</div>
<div class="abs socials"><i></i><i></i><i></i><i></i></div>
<nav class="abs nav"><span>HOME</span><span>ABOUT US</span><span>SERVICES</span><span>TEAM</span><span>BLOG</span><span>CONTACT US</span></nav>
<div class="abs quote-btn">GET A QUOTE</div>

<!-- hero -->
<div class="abs hero" role="img" aria-label="Photo of a plumber hydro-jetting a drain with a high pressure water spray"></div>
<div class="abs hero-shade"></div>
<h1 class="abs hero-title">TIRED OF WAITING<br>FOR A PLUMBER?</h1>
<p class="abs hero-sub">Call Us For A Fast Professional And Same Day Service</p>
<div class="abs hero-btn">CALL US TODAY</div>
<form class="abs form">
  <h3>GET A QUOTE</h3>
  <div class="field">NAME</div>
  <div class="field">PHONE</div>
  <div class="field">EMAIL</div>
  <div class="field tall">HOW CAN WE HELP?</div>
  <div class="submit">SUBMIT INQUIRY</div>
</form>
<svg class="abs wave" viewBox="0 0 1200 165" preserveAspectRatio="none">
  <path d="M0 110 C200 40 380 40 600 95 S1000 150 1200 60 L1200 165 L0 165Z" fill="#d9d9d9" opacity=".7"/>
  <path d="M0 130 C220 70 400 70 620 115 S1000 160 1200 90 L1200 165 L0 165Z" fill="#fff"/>
</svg>

<!-- features -->
<div class="abs feature" style="left:120px">
  <div class="ico" style="background:#e8b51e"><svg width="50" height="50" viewBox="0 0 50 50" fill="none" stroke="#fff" stroke-width="3"><path d="M10 40 L22 28 M22 20 h12 v10 h-12z M34 25 h8"/></svg></div>
  <h4>NO-DIG DRAIN REPAIR</h4>
  <p>Lorem Ipsum is simply dummy text of the printing and typesetting industry.</p>
</div>
<div class="abs feature" style="left:446px">
  <div class="ico" style="background:var(--red)"><svg width="50" height="50" viewBox="0 0 50 50" fill="none" stroke="#fff" stroke-width="3"><path d="M14 36 L30 20 M30 20 a7 7 0 1 0 6-10 l-4 4 -4-1 -1-4 4-4 a7 7 0 0 0-10 6"/><path d="M12 12 l26 26"/></svg></div>
  <h4>REPAIRS ALL PIPE TYPES</h4>
  <p>Lorem Ipsum is simply dummy text of the printing and typesetting industry.</p>
</div>
<div class="abs feature" style="left:774px">
  <div class="ico" style="background:#1ea1e4"><svg width="50" height="50" viewBox="0 0 50 50" fill="none" stroke="#fff" stroke-width="3"><circle cx="25" cy="18" r="8"/><path d="M10 42 c2-10 28-10 30 0"/></svg></div>
  <h4>SAME DAY SERVICE</h4>
  <p>Lorem Ipsum is simply dummy text of the printing and typesetting industry.</p>
</div>
<div class="abs band"></div>

<!-- residential -->
<section class="abs panel" style="top:1192px;background:var(--light)"></section>
<div class="abs photo" style="left:546px;top:1192px;width:654px;background:linear-gradient(135deg,#6b5a45,#9a8f7c 50%,#4f5a4a);clip-path:polygon(0 0,100% 0,100% 100%,6% 100%)" role="img" aria-label="Photo of a plumber working on an outdoor pipe"></div>
<h2 class="abs svc-title" style="left:142px;top:1236px">RESIDENTIAL<em>Plumbing</em></h2>
<div class="abs rule" style="left:142px;top:1358px"></div>
<div class="abs copy" style="left:142px;top:1378px">
  <p>Lorem ipsum dolor sit amet, consectetuer adipiscing elit, sed diam nonummy nibh euismod tincidunt ut laoreet dolore magna aliquam erat volutpat. Ut wisi enim ad minim veniam, quis nostrud exerci tation ullamcorper suscipit lobortis nisl ut aliquip ex ea augue duis feugait nulla facilisi.</p>
  <p>Lorem ipsum dolor sit amet, consectetuer adipiscing elit, sed diam nonummy nibh .</p>
</div>
<div class="abs more" style="left:142px;top:1608px">READ MORE ›</div>

<!-- commercial -->
<section class="abs panel on-blue" style="top:1706px;background:var(--blue)"></section>
<div class="abs photo" style="left:0;top:1706px;width:640px;background:linear-gradient(160deg,#c9c3b3,#8a7a5d 55%,#4b3c2a);clip-path:polygon(0 0,100% 0,90% 100%,0 100%)" role="img" aria-label="Photo of a copper backflow valve assembly outside a building"></div>
<div class="on-blue">
  <h2 class="abs svc-title" style="left:658px;top:1752px">COMMERCIAL<em style="margin-left:120px">Plumbing</em></h2>
  <div class="abs copy" style="left:658px;top:1896px;width:400px">
    <p>Lorem ipsum dolor sit amet, consectetuer adipiscing elit, sed diam nonummy nibh euismod tincidunt ut laoreet dolore magna aliquam erat volutpat. Ut wisi enim ad minim veniam, quis nostrud exerci tation ullamcorper suscipit lobortis nisl ut aliquip ex ea augue duis feugait nulla facilisi.</p>
    <p>Lorem ipsum dolor sit amet, consectetuer adipiscing elit, sed diam nonummy nibh .</p>
  </div>
</div>
<div class="abs more" style="left:658px;top:2126px">READ MORE ›</div>

<!-- appliance -->
<section class="abs panel" style="top:2220px;height:498px;background:var(--white)"></section>
<div class="abs photo" style="left:552px;top:2220px;width:648px;height:498px;background:linear-gradient(150deg,#7f9a6a,#b7c0b8 45%,#e8ecec 70%,#6d6f6a);clip-path:polygon(0 0,100% 0,100% 100%,5% 100%)" role="img" aria-label="Photo of white service vans parked in a driveway"></div>
<h2 class="abs svc-title" style="left:142px;top:2290px">APPLIANCE<em style="margin-left:110px">Repairs</em></h2>
<div class="abs rule" style="left:142px;top:2390px"></div>
<div class="abs copy" style="left:142px;top:2410px">
  <p>Lorem ipsum dolor sit amet, consectetuer adipiscing elit, sed diam nonummy nibh euismod tincidunt ut laoreet dolore magna aliquam erat volutpat. Ut wisi enim ad minim veniam, quis nostrud exerci tation ullamcorper suscipit lobortis nisl ut aliquip ex ea augue duis feugait nulla facilisi.</p>
  <p>Lorem ipsum dolor sit amet, consectetuer adipiscing elit, sed diam nonummy nibh .</p>
</div>
<div class="abs more" style="left:142px;top:2646px">READ MORE ›</div>

<!-- additional services -->
<section class="abs additional"></section>
<h2 class="abs sec-title" style="left:0;top:2772px">ADDITIONAL <em>Services</em></h2>
<div class="abs rule" style="left:582px;top:2840px"></div>

<div class="abs svc" style="left:200px;top:2870px">
  <div class="badge"><svg width="30" height="30" viewBox="0 0 30 30" fill="none" stroke="#1d77c8" stroke-width="2"><path d="M4 12h12v6H4zM16 15h8v10M10 8v4"/></svg></div>
  <h5>Gas &amp; Waterline<br>Replacement</h5>
  <p>Lorem ipsum dolor sit amet, consectetuer adipiscing elit, sed tincidunt ut laoreet</p>
</div>
<div class="abs svc" style="left:510px;top:2870px">
  <div class="badge"><svg width="30" height="30" viewBox="0 0 30 30" fill="none" stroke="#1d77c8" stroke-width="2"><rect x="5" y="8" width="20" height="6"/><rect x="5" y="17" width="20" height="6"/></svg></div>
  <h5>Sewer Line Repair<br>&amp; Replacement</h5>
  <p>Lorem ipsum dolor sit amet, consectetuer adipiscing elit, sed tincidunt ut laoreet</p>
</div>
<div class="abs svc" style="left:820px;top:2870px">
  <div class="badge"><svg width="30" height="30" viewBox="0 0 30 30" fill="none" stroke="#1d77c8" stroke-width="2"><rect x="5" y="5" width="20" height="20"/><path d="M5 12h20M12 12v13"/></svg></div>
  <h5>New Construction</h5>
  <p>Lorem ipsum dolor sit amet, consectetuer adipiscing elit, sed tincidunt ut laoreet</p>
</div>
<div class="abs svc" style="left:200px;top:3126px">
  <div class="badge"><svg width="30" height="30" viewBox="0 0 30 30" fill="none" stroke="#1d77c8" stroke-width="2"><path d="M8 4v10a7 7 0 0014 0V4M15 21v6"/></svg></div>
  <h5>Drain Cleaning</h5>
  <p>Lorem ipsum dolor sit amet, consectetuer adipiscing elit, sed tincidunt ut laoreet</p>
</div>
<div class="abs svc" style="left:510px;top:3126px">
  <div class="badge"><svg width="30" height="30" viewBox="0 0 30 30" fill="none" stroke="#1d77c8" stroke-width="2"><rect x="8" y="4" width="10" height="22" rx="2"/><circle cx="22" cy="8" r="3"/></svg></div>
  <h5>Leak Detection</h5>
  <p>Lorem ipsum dolor sit amet, consectetuer adipiscing elit, sed tincidunt ut laoreet</p>
</div>
<div class="abs all-card">
  <h5>ALL OUR SERVICES</h5>
  <p>Get a get a detailed overview of all the services we offer now.</p>
  <div class="more">VIEW SERVICES ›</div>
</div>

<!-- testimonials -->
<h2 class="abs sec-title" style="left:0;top:3444px">WHAT OUR <em>Clients Saying</em></h2>
<svg class="abs arrow" style="left:118px" width="20" height="36" viewBox="0 0 20 36"><path d="M16 2L3 18l13 16" fill="none" stroke="#bbb" stroke-width="2"/></svg>
<svg class="abs arrow" style="left:1062px" width="20" height="36" viewBox="0 0 20 36"><path d="M4 2l13 16L4 34" fill="none" stroke="#bbb" stroke-width="2"/></svg>
<div class="abs tcard" style="left:188px"><span class="q">“</span>
  <blockquote>"Best customer service ever! From the appointment maker to the actual service person, the customer was out was out-standing! Will use as long."</blockquote>
  <h6>Mara Ellison</h6><div class="co">Company Name</div></div>
<div class="abs tcard active" style="left:466px"><span class="q">“</span>
  <blockquote>"Best customer service ever! From the appointment maker to the actual service person, the customer was out was out-standing! Will use as long."</blockquote>
  <h6>Reno D.</h6><div class="co">Company Name</div></div>
<div class="abs tcard" style="left:745px"><span class="q">“</span>
  <blockquote>"Best customer service ever! From the appointment maker to the actual service person, the customer was out was out-standing! Will use as long."</blockquote>
  <h6>Lena K.</h6><div class="co">Company Name</div></div>
<div class="abs dots"><i class="on"></i><i></i><i></i></div>

<!-- footer -->
<footer class="abs footer"></footer>
<div class="abs fcol" style="left:143px">
  <h6>Our Services</h6>
  <ul><li>Plumbing</li><li>Heating</li><li>Kitchen &amp; Bath Remodeling</li><li>Appliance Repair</li></ul>
</div>
<div class="abs fcol" style="left:384px">
  <h6>Quick Links</h6>
  <ul><li>Home</li><li>About us</li><li>Residential</li><li>Commercial</li></ul>
</div>
<div class="abs fcol" style="left:590px">
  <h6>Contact Details</h6>
  <div class="row"><svg width="12" height="16" viewBox="0 0 12 16"><path d="M6 0a6 6 0 00-6 6c0 4.5 6 10 6 10s6-5.5 6-10a6 6 0 00-6-6zm0 8.5A2.5 2.5 0 116 3.5a2.5 2.5 0 010 5z" fill="#fff"/></svg><span>48 Harbor Lane, Suite 2,<br>Bayview</span></div>
  <div class="row"><svg width="12" height="12" viewBox="0 0 24 24"><path d="M6.6 10.8a15.1 15.1 0 006.6 6.6l2.2-2.2a1 1 0 011-.25 11.4 11.4 0 003.6.57 1 1 0 011 1V20a1 1 0 01-1 1A17 17 0 013 4a1 1 0 011-1h3.5a1 1 0 011 1c0 1.25.2 2.45.57 3.57a1 1 0 01-.25 1z" fill="#fff"/></svg><span>+1 555 014 2290</span></div>
  <div class="row"><svg width="13" height="10" viewBox="0 0 13 10"><rect x=".5" y=".5" width="12" height="9" fill="none" stroke="#fff"/><path d="M.5.5l6 5 6-5" fill="none" stroke="#fff"/></svg><span>info@keelwaterplumbing.com</span></div>
</div>
<div class="abs fcol" style="left:847px">
  <h6>Newsletter</h6>
  <div style="color:#fff;font-size:11.5px">Lorem Epsum is simply dummy printing</div>
  <div class="news-in">Put your Email here <span style="color:var(--red);font-size:16px">⟶</span></div>
  <div class="fsocial"><i></i><i></i><i></i><i></i></div>
</div>
<div class="abs footbar">© 2019 Keelwater Plumbing. All Rights Reserved</div>

</body>
</html>
```